International IT Business Needs a Proffesional and Innovative Business Card

We need a proffesional and innovative business card for a new company based in Venezuela called 'QuillonMark'. We are RVK Business Partner, RVK is a key manufacture for us, one of the most influential players in technology, and the leader in cloud computing, virtualization, Big Data storage and analytics, and IT security and protection.

RVK has developed a global network of business partners to bring customers the full complement of skills and expertise required to build their information infrastructures. This partner ecosystem helps customers maximize the value of their information at the lowest total cost.

We would like to see designs that use the RVK Business Partnet logo & QuillonMark logo.

http://brand.rvk-example.com/BrandGuide/partners/rvk-business-partner-logo/

Thank you in advance for your interest.

Happy Day!!!! I look forward to your creative design!!!

Thank you in advance.

Marisol Quevedo

Target Market(s)

QuillonMark's target markets include large companies and small- and medium-sized businesses across various vertical markets.

Industry/Entity Type

Security

Font styles to use
Other font styles liked:
• We use Meta as the RVK® corporate font.

Colors

Designer to choose colors to be used in the design.

Requirements
Must have
• Name
Title
Address
web page (www.quillon-example.la)

Nice to have
• Add a QR code on the reverse of the card.

```html
<!DOCTYPE html>
<html lang="en">
<head>
<meta charset="utf-8">
<title>QuillonMark Business Card</title>
<link rel="stylesheet" href="https://fonts.googleapis.com/css2?family=Libre+Baskerville:ital,wght@0,700;1,400&family=Source+Sans+3:wght@400;700&display=swap">
<style>
  :root {
    --backdrop: #b9bbba;
    --card-front: #e8e8e7;
    --card-back: #f3f3f1;
    --navy: #2a2260;
    --green-dark: #17963f;
    --green-light: #6db33a;
    --divider: #cfcfcd;
    --text-light: #ffffff;
    --accent: #8cc63f;
  }
  * { box-sizing: border-box; margin: 0; padding: 0; }
  html, body { width: 1200px; height: 900px; overflow: hidden; }
  body {
    background: var(--backdrop);
    font-family: "Source Sans 3", Arial, sans-serif;
    display: flex;
    flex-direction: column;
    align-items: center;
    justify-content: center;
    gap: 40px;
  }
  .card {
    position: relative;
    width: 700px;
    height: 400px;
    overflow: hidden;
    box-shadow: 0 6px 18px rgba(0,0,0,0.18);
  }
  .card--front { background: var(--card-front); }
  .card--back { background: var(--card-back); }

  .brand {
    position: absolute;
    display: flex;
    align-items: center;
    gap: 12px;
    font-weight: 700;
    color: var(--navy);
    letter-spacing: 0.5px;
  }
  .brand__dot { border-radius: 50%; background: var(--green-dark); }
  .card--front .brand { left: 50%; top: 120px; transform: translateX(-50%); font-size: 46px; }
  .card--front .brand__dot { width: 30px; height: 30px; }
  .card--back .brand { left: 48px; top: 110px; font-size: 34px; }
  .card--back .brand__dot { width: 22px; height: 22px; }

  .divider { position: absolute; left: 0; right: 0; background: var(--divider); }
  .green-band {
    position: absolute; left: 0; right: 0; bottom: 0;
    background: linear-gradient(90deg, var(--green-dark), var(--green-light));
  }
  .card--front .divider { top: 292px; height: 14px; }
  .card--front .green-band { height: 94px; }
  .card--back .divider { top: 334px; height: 10px; }
  .card--back .green-band { height: 56px; }

  .person { position: absolute; right: 48px; top: 40px; text-align: right; }
  .person__name {
    font-family: "Libre Baskerville", Georgia, serif;
    font-weight: 700; font-size: 24px; color: var(--navy); letter-spacing: 1px;
  }
  .person__title {
    font-family: "Libre Baskerville", Georgia, serif;
    font-style: italic; font-size: 13px; color: var(--green-light); margin-top: 4px;
  }

  .contact-band {
    position: absolute; left: 0; right: 0; top: 226px; height: 108px;
    background: var(--navy);
    display: flex; align-items: center; justify-content: space-around;
    padding: 0 28px;
    color: var(--text-light); font-size: 14px; line-height: 1.6;
  }
  .contact-group { display: flex; flex-direction: column; gap: 6px; }
  .contact-item { display: flex; align-items: flex-start; gap: 10px; }
  .contact-item svg { width: 14px; height: 14px; flex: none; margin-top: 4px; }
</style>
</head>
<body>
  <section class="card card--front" aria-label="Card front">
    <div class="brand"><span class="brand__dot"></span>QuillonMark</div>
    <div class="divider"></div>
    <div class="green-band"></div>
  </section>

  <section class="card card--back" aria-label="Card back">
    <div class="brand"><span class="brand__dot"></span>QuillonMark</div>
    <div class="person">
      <p class="person__name">DORIAN VALE</p>
      <p class="person__title">Graphic Designer</p>
    </div>
    <div class="contact-band">
      <div class="contact-group">
        <div class="contact-item">
          <svg viewBox="0 0 14 14" aria-hidden="true"><path d="M7 0a5 5 0 0 0-5 5c0 3.5 5 9 5 9s5-5.5 5-9a5 5 0 0 0-5-5zm0 7a2 2 0 1 1 0-4 2 2 0 0 1 0 4z" fill="var(--accent)"/></svg>
          <span>482 Lindenmoor Ave,<br>Westbrook, NY 54321</span>
        </div>
      </div>
      <div class="contact-group">
        <div class="contact-item">
          <svg viewBox="0 0 14 14" aria-hidden="true"><path d="M3 1l2 3-1.3 1.3a8 8 0 0 0 5 5L10 9l3 2-1.5 2.5C6 13 1 8 .5 2.5z" fill="var(--accent)"/></svg>
          <span>+(000) 5550 1842</span>
        </div>
        <div class="contact-item">
          <svg viewBox="0 0 14 14" aria-hidden="true"><rect x="3" y="1" width="8" height="4" fill="var(--accent)"/><rect x="1" y="5" width="12" height="6" rx="1" fill="var(--accent)"/><rect x="3" y="9" width="8" height="4" fill="#fff"/></svg>
          <span>+(000) 5550 1843</span>
        </div>
      </div>
      <div class="contact-group">
        <div class="contact-item">
          <svg viewBox="0 0 14 14" aria-hidden="true"><circle cx="7" cy="7" r="6" fill="none" stroke="var(--accent)" stroke-width="1.4"/><path d="M1 7h12M7 1c-3 3.5-3 8.5 0 12M7 1c3 3.5 3 8.5 0 12" fill="none" stroke="var(--accent)" stroke-width="1.2"/></svg>
          <span>www.quillon-example.la</span>
        </div>
        <div class="contact-item">
          <svg viewBox="0 0 14 14" aria-hidden="true"><rect x="1" y="3" width="12" height="8" fill="none" stroke="var(--accent)" stroke-width="1.4"/><path d="M1 3l6 5 6-5" fill="none" stroke="var(--accent)" stroke-width="1.4"/></svg>
          <span>dorian.vale@quillon-example.la</span>
        </div>
      </div>
    </div>
    <div class="divider"></div>
    <div class="green-band"></div>
  </section>
</body>
</html>
```